Brisco Energy PowerPoint Design

Looking for a sleek PowerPoint design for our energy services company. We supply EV charging, Solar, Battery Storage and more.

Please make the background white with hints of gray and utilize the exact dark blue and light blue colors in the logo.

This design should be sharp with minimal round edges.

Colors

Designer to choose colors to be used in the design.

```html
<!DOCTYPE html>
<html lang="en">
<head>
<meta charset="utf-8">
<title>Brisco Energy – Presentation Slides</title>
<link href="https://fonts.googleapis.com/css2?family=Oswald:wght@400;500;600&family=Roboto:wght@400;500;700&family=Courier+Prime:wght@700&display=swap" rel="stylesheet">
<style>
:root{
  --navy:#1b1763;
  --sky:#3bb4ef;
  --sky-soft:#4a8fd0;
  --green:#8dc63f;
  --olive:#5a7a3a;
  --ink:#222630;
  --muted:#6b6f78;
  --paper:#ffffff;
  --mist:#eef1f4;
  --stage:#000000;
}
*{margin:0;padding:0;box-sizing:border-box}
html,body{width:876px;height:1200px;overflow:hidden;background:var(--stage)}
body{position:relative;font-family:'Roboto',sans-serif;color:var(--ink)}
.slide{position:absolute;width:373px;height:209px;background:var(--paper);overflow:hidden}
.col-a{left:60px}.col-b{left:450px}
.row-1{top:53px}.row-2{top:278px}.row-3{top:504px}.row-4{top:729px}.row-5{top:955px}
.abs{position:absolute}
.fill{position:absolute}
/* footer band */
.footer{position:absolute;left:0;right:0;bottom:0;height:16px;background:var(--navy);color:#fff;font-family:'Oswald',sans-serif;font-size:7.5px;letter-spacing:1.2px}
.footer .brand{position:absolute;left:36px;top:3px}
.footer .brand span{font-weight:400;opacity:.85}
.footer .brand b{font-weight:600}
.footer .num{position:absolute;right:13px;top:3px;opacity:.8}
/* side rail */
.rail{position:absolute;left:12px;top:20px;bottom:24px;width:1px;background:#c9ccd2}
.rail-year{position:absolute;left:3px;width:20px;text-align:center;font-family:'Roboto',sans-serif;font-weight:700;font-size:8px;color:var(--navy);transform:rotate(-90deg);background:var(--paper)}
.rail-dot{position:absolute;left:7px;width:11px;height:16px;border:1px solid #c9ccd2;border-radius:6px;background:var(--paper)}
/* brand word */
.brand-word{font-family:'Roboto',sans-serif;font-weight:700;color:var(--navy);letter-spacing:.3px;display:flex;align-items:center;gap:4px}
.brand-word i{display:inline-block;background:var(--navy)}
/* mono heading */
.mono{font-family:'Courier Prime',monospace;font-weight:700;color:var(--ink);line-height:1.15}
.mark{background:var(--sky-soft);padding:0 1px}
/* slide 1 */
.cover{background:linear-gradient(120deg,#e4edf1,#f3f6f8 60%,#e9eef2)}
.cover .title{position:absolute;left:211px;top:94px;font-family:'Roboto',sans-serif;font-weight:500;font-size:15px;color:var(--ink);letter-spacing:.3px}
.cover .year{position:absolute;left:218px;top:120px;font-weight:700;font-size:18px;color:var(--navy)}
.cover .rule{position:absolute;left:216px;top:115px;width:110px;height:1px;background:var(--sky)}
/* agenda */
.agenda .head{position:absolute;left:33px;top:55px;font-size:12px}
.agenda ul{position:absolute;left:33px;top:74px;list-style:none;font-size:8px;color:var(--ink);line-height:1}
.agenda li{display:flex;align-items:flex-start;gap:5px;margin-bottom:5.5px}
.agenda li svg{flex:none}
/* slide 3 */
.tile{position:absolute;top:22px;width:68px;height:162px;overflow:hidden}
.tile .cap{position:absolute;left:0;right:0;bottom:0;display:flex;align-items:center;justify-content:center;text-align:center;font-weight:500;line-height:1.2;padding:0 5px}
/* slide 4 grid */
.cell{position:absolute;width:93px;height:64px;display:flex;flex-direction:column;align-items:center;justify-content:center;text-align:center;font-family:'Roboto',sans-serif;font-weight:500;font-size:7px;line-height:1.05;color:var(--ink);gap:4px}
/* slide 5 */
.stat-card{position:absolute;left:35px;top:25px;width:88px;height:162px;background:var(--navy);border:1.5px solid #fff;color:#fff;text-align:center;font-weight:700}
/* slide 6 */
.disc{position:absolute;border-radius:50%;display:flex;align-items:center;justify-content:center;text-align:center;font-family:'Oswald',sans-serif;font-size:7.5px;line-height:1.15}
/* roadmap */
.road-label{position:absolute;font-size:6.5px;color:var(--ink);text-align:center;line-height:1.3}
.road-label b{font-size:7.5px;font-weight:700;display:block}
/* team */
.member{position:absolute;top:52px;width:76px;height:101px;overflow:hidden}
.member .name{position:absolute;left:0;right:0;bottom:5px;text-align:center;color:#fff;font-family:'Oswald',sans-serif;font-size:7px}
.member .name::after{content:"";display:block;width:22px;height:1.5px;background:var(--sky);margin:2px auto 0}
.values{position:absolute;left:63px;top:171px;display:flex;gap:11px;font-family:'Roboto',sans-serif;font-weight:500;font-size:7.5px}
.values span{display:flex;align-items:center;gap:3px}
.values i{width:9px;height:9px;border:1px solid #888;border-radius:50%;display:inline-block}
/* services */
.svc-box{position:absolute;left:31px;top:45px;width:142px;height:72px;background:#263140;padding:5px 8px;list-style:none;color:#fff;font-size:6.3px;line-height:1.55}
.svc-list{position:absolute;left:181px;top:69px;list-style:none;font-size:6.3px;line-height:1.5;color:var(--ink)}
.svc-box li::before,.svc-list li::before{content:"› ";color:var(--sky)}
/* closing */
.close-wrap{position:absolute;left:0;right:0;top:60px;text-align:center}
</style>
</head>
<body>

<!-- Slide: cover -->
<section class="slide col-a row-1 cover">
  <div class="fill" role="img" aria-label="Glowing light bulb in soil with seedlings and rising bar graph" style="inset:0;clip-path:polygon(0 0,120px 0,240px 209px,0 209px);background:linear-gradient(160deg,#0e3d44,#1b6a6e 45%,#2c8a7c 70%,#123a3a)"></div>
  <svg class="abs" style="left:0;top:0" width="373" height="209" viewBox="0 0 373 209">
    <polygon points="120,0 128,0 248,209 240,209" fill="var(--green)"/>
    <polygon points="0,127 53,209 0,209" fill="var(--green)"/>
  </svg>
  <div class="brand-word abs" style="left:211px;top:67px;font-size:13px"><i style="width:10px;height:10px"></i>Brisco Energy</div>
  <div class="title">BRISCO ENERGY</div>
  <div class="rule"></div>
  <div class="year">2025</div>
</section>

<!-- Slide: agenda -->
<section class="slide col-b row-1 agenda">
  <div class="rail"></div>
  <div class="rail-year" style="top:90px">2023</div>
  <div class="rail-dot" style="top:110px"></div>
  <div class="head mono"><span class="mark">AGEN</span>DA</div>
  <ul>
    <li><svg width="10" height="9" viewBox="0 0 10 9"><circle cx="3" cy="2.5" r="1.8" fill="var(--ink)"/><circle cx="7" cy="2.5" r="1.8" fill="var(--ink)"/><rect x="0.5" y="5" width="4.5" height="4" fill="var(--ink)"/><rect x="5" y="5" width="4.5" height="4" fill="var(--ink)"/></svg><span>WHY A FAMILY<br>OFFICE</span></li>
    <li><svg width="10" height="9" viewBox="0 0 10 9" fill="none" stroke="var(--ink)" stroke-width=".8"><circle cx="5" cy="2.5" r="1.8"/><circle cx="2" cy="5" r="1.4"/><circle cx="8" cy="5" r="1.4"/><path d="M0.5 9h9"/></svg><span>OUR TEAM</span></li>
    <li><svg width="10" height="9" viewBox="0 0 10 9" fill="none" stroke="var(--ink)" stroke-width=".8"><circle cx="3" cy="3" r="2"/><path d="M0.5 9c0-2 5-2 5 0"/><rect x="6" y="1" width="3.5" height="3"/></svg><span>OUR SERVICES</span></li>
    <li><svg width="10" height="9" viewBox="0 0 10 9"><rect x="0.5" y="0.5" width="9" height="2" fill="#d9a21b"/><rect x="0.5" y="3.5" width="9" height="2" fill="#d9a21b"/><rect x="0.5" y="6.5" width="9" height="2" fill="#d9a21b"/></svg><span>OUR PROCESS</span></li>
    <li><svg width="10" height="9" viewBox="0 0 10 9" fill="none" stroke="var(--ink)" stroke-width=".8"><path d="M0.5 5l3-2 3 2 3-2M1 5l4 3 4-3"/><circle cx="5" cy="1.5" r="1"/></svg><span>FAMILY &amp; PARTNER<br>FEEDBACK</span></li>
  </ul>
  <div class="fill" role="img" aria-label="Illustration of a businesswoman and businessman with dollar signs, calculator, chart and dashed arrows" style="left:178px;top:8px;width:188px;height:185px;background:radial-gradient(ellipse at 60% 70%,#2c8a8a 0%,#3a6e8a 35%,#e8f3f4 70%,#fff 100%)"></div>
  <div class="footer"><div class="brand"><b>BRISCO</b> <span>ENERGY</span></div><div class="num">01</div></div>
</section>

<!-- Slide: image columns -->
<section class="slide col-a row-2">
  <div class="rail"></div>
  <div class="rail-year" style="top:80px">2025</div>
  <div class="rail-dot" style="top:100px"></div>
  <div class="brand-word abs" style="left:10px;top:96px;font-size:9px;transform:rotate(-90deg);transform-origin:center;width:70px;justify-content:center"><i style="width:7px;height:7px"></i>Brisco Energy</div>
  <div class="tile" style="left:64px;border:1px solid var(--sky)" role="img" aria-label="Solar panels beneath pine trees and a blue sky" ><div class="fill" style="inset:0;background:linear-gradient(180deg,#5fb6d8 0%,#5a8a5a 45%,#3b6a8a 70%,#2a3f6a 100%)"></div></div>
  <div class="tile" style="left:136px">
    <div class="fill" role="img" aria-label="Hands under running water from a tap" style="left:0;right:0;top:0;height:115px;background:linear-gradient(160deg,#6b3b22,#b8794d 55%,#3a2518)"></div>
    <div class="cap" style="height:47px;background:#d9d9d9;font-size:6.5px;color:var(--ink)">LOREM IPSUM IS SIMPLY TEXT OF THE PRINTING</div>
  </div>
  <div class="tile" style="left:208px">
    <div class="fill" role="img" aria-label="Floating solar panels on a lake with hills" style="left:0;right:0;top:0;height:95px;background:linear-gradient(180deg,#9fc1dc 0%,#8aa9c0 35%,#3d5f8f 60%,#1d3b6e 100%)"></div>
    <div class="cap" style="height:67px;background:#8a8a8a;color:#fff;font-size:7.5px">LOREM IPSUM IS SIMPLY TEXT OF THE PRINTING</div>
  </div>
  <div class="tile" style="left:280px">
    <div class="fill" role="img" aria-label="Red tractor in a sugar cane field" style="left:0;right:0;top:0;height:71px;background:linear-gradient(180deg,#a8c2cf 0%,#7a8c5a 40%,#9a4a3a 65%,#4d5a3a 100%)"></div>
    <div class="cap" style="height:91px;background:var(--sky);color:#fff;font-size:7.5px">LOREM IPSUM IS SIMPLY TEXT OF THE PRINTING</div>
  </div>
  <div class="footer"><div class="brand"><b>BRISCO</b> <span>ENERGY</span></div><div class="num">02</div></div>
</section>

<!-- Slide: why a family office grid -->
<section class="slide col-b row-2">
  <div class="cell" style="left:0;top:0">
    <svg width="28" height="22" viewBox="0 0 28 22" fill="none" stroke="var(--ink)" stroke-width="1.4"><circle cx="7" cy="5" r="3" fill="var(--ink)"/><path d="M1 20v-6c0-3 12-3 12 0v6z" fill="var(--ink)"/><circle cx="20" cy="8" r="5"/><path d="M24 12l3 3"/></svg>
    PROFESSIONAL<br>EXPERTISE</div>
  <div class="fill" role="img" aria-label="Black and white photo of a business team reviewing documents" style="left:93px;top:0;width:93px;height:64px;background:linear-gradient(135deg,#d8d8d8,#6a6a6a 55%,#2a2a2a)"></div>
  <div class="cell" style="left:186px;top:0">
    <svg width="28" height="22" viewBox="0 0 28 22" fill="none" stroke="var(--ink)" stroke-width="1.2"><rect x="8" y="1" width="12" height="6"/><circle cx="7" cy="13" r="2.5"/><circle cx="14" cy="13" r="2.5"/><circle cx="21" cy="13" r="2.5"/><path d="M2 21c0-4 10-4 10 0M9 21c0-4 10-4 10 0M16 21c0-4 10-4 10 0"/></svg>
    CUSTOMIZED<br>SOLUTIONS</div>
  <div class="fill" role="img" aria-label="Black and white photo of a notebook with a written solution diagram and keyboard" style="left:279px;top:0;width:94px;height:64px;background:linear-gradient(150deg,#3a3a3a,#bdbdbd 50%,#f0f0f0)"></div>

  <div class="fill" role="img" aria-label="Black and white photo of a computer screen with privacy shield" style="left:0;top:64px;width:93px;height:64px;background:linear-gradient(135deg,#4a4a4a,#cfcfcf 60%,#8a8a8a)"></div>
  <div class="cell" style="left:93px;top:64px;background:var(--sky)">
    <svg width="22" height="24" viewBox="0 0 22 24" fill="none" stroke="var(--ink)" stroke-width="1.2"><rect x="2" y="1" width="16" height="20"/><path d="M10 4l4 2v3c0 3-4 5-4 5s-4-2-4-5V6z"/><rect x="12" y="15" width="8" height="7"/><path d="M14 15v-2a2 2 0 014 0v2"/></svg>
    CONFIDENTIALITY</div>
  <div class="abs" style="left:201px;top:70px;width:170px">
    <div class="mono" style="font-size:11.5px"><span class="mark">WHY A</span> FAMILY<br>OFFICE?</div>
    <p style="font-size:4.3px;color:#333;margin-top:4px;line-height:1.5">Family offices offer comprehensive solutions to manage ultra-high net-worth families' complex financial needs.<br>Some of the primary benefits offered by a family office include –</p>
  </div>

  <div class="cell" style="left:0;top:128px">
    <svg width="26" height="24" viewBox="0 0 26 24" fill="none" stroke="var(--ink)" stroke-width="1.2"><rect x="3" y="1" width="8" height="5"/><rect x="14" y="1" width="8" height="5"/><circle cx="7" cy="11" r="2"/><circle cx="18" cy="11" r="2"/><rect x="2" y="15" width="22" height="3"/><path d="M5 18v5M21 18v5"/></svg>
    OBJECTIVE<br>ADVICE</div>
  <div class="fill" role="img" aria-label="Black and white photo of hands over a business plan paper" style="left:93px;top:128px;width:93px;height:65px;background:linear-gradient(160deg,#6a6a6a,#e6e6e6 55%,#cfcfcf)"></div>
  <div class="cell" style="left:186px;top:128px">
    <svg width="30" height="24" viewBox="0 0 30 24" fill="none" stroke="var(--ink)" stroke-width="1.2"><circle cx="8" cy="6" r="2.5"/><circle cx="22" cy="6" r="2.5"/><rect x="12" y="0.5" width="6" height="5" rx="2"/><path d="M3 12c0-3 10-3 10 0M17 12c0-3 10-3 10 0"/><circle cx="8" cy="16" r="2.5"/><circle cx="22" cy="16" r="2.5"/><path d="M3 23c0-3 10-3 10 0M17 23c0-3 10-3 10 0"/></svg>
    COMMUNICATION &amp;<br>CUSTOMER SERVICE</div>
  <div class="fill" role="img" aria-label="Black and white photo of people working with headsets at laptops" style="left:279px;top:128px;width:94px;height:65px;background:linear-gradient(120deg,#f2f2f2,#9a9a9a 55%,#4a4a4a)"></div>
  <div class="footer"><div class="brand"><b>BRISCO</b> <span>ENERGY</span></div><div class="num">03</div></div>
</section>

<!-- Slide: solar field with stats -->
<section class="slide col-a row-3">
  <div class="fill" role="img" aria-label="Rows of solar panels in a grassy field under a cloudy sky" style="inset:0;background:linear-gradient(180deg,#bcd3ea 0%,#e9eff5 35%,#9fb0cc 55%,#5d6f9f 75%,#4d6a4a 100%)"></div>
  <div class="rail"></div>
  <div class="rail-year" style="top:90px;background:transparent">2025</div>
  <div class="rail-dot" style="top:110px"></div>
  <div class="stat-card">
    <svg style="margin-top:10px" width="18" height="12" viewBox="0 0 18 12"><path d="M1 11h16M3 11V6h12v5" fill="none" stroke="var(--sky)" stroke-width="1.2"/><path d="M6 6V2h6v4" fill="var(--sky)"/></svg>
    <div style="font-size:7.5px;line-height:1.25;margin-top:5px">23.000 km di<br>canali in Italia</div>
    <svg style="margin-top:5px" width="18" height="18" viewBox="0 0 18 18" fill="none" stroke="#fff" stroke-width=".8"><circle cx="9" cy="9" r="8.3"/><rect x="5" y="5" width="8" height="7"/><path d="M5 8h8M9 5v7"/></svg>
    <div style="font-size:5.6px;line-height:1.3;margin-top:3px;padding:0 4px">Canali non soggetti a vincoli e con adeguate specifiche tecniche</div>
    <svg style="margin-top:7px" width="18" height="18" viewBox="0 0 18 18" fill="none" stroke="#fff" stroke-width=".8"><circle cx="9" cy="9" r="8.3"/><path d="M4 12l5-6 5 6M6 12v-3M12 12v-3"/></svg>
    <div style="font-size:5px;line-height:1.3;margin-top:3px;padding:0 4px">Utenze in prossimità di canali (PMI, Aziende agricole) che necessitano di Energia Elettrica</div>
  </div>
  <div class="brand-word abs" style="left:134px;top:77px;font-size:10px"><i style="width:8px;height:8px"></i>Brisco Energy</div>
  <div class="abs" style="left:134px;top:110px;font-weight:700;font-size:11.5px;color:var(--navy);line-height:1.3">LOREM IPSUM IS<br>SIMPLY</div>
  <div class="footer"><div class="brand"><b>BRISCO</b> <span>ENERGY</span></div><div class="num">04</div></div>
</section>

<!-- Slide: why our family office -->
<section class="slide col-b row-3">
  <div class="rail"></div>
  <div class="rail-year" style="top:90px">2025</div>
  <div class="rail-dot" style="top:110px"></div>
  <div class="abs mono" style="left:31px;top:33px;font-size:13px"><span class="mark">WHY OU</span>R FAMILY<br>&nbsp;OFFICE?</div>
  <div class="abs" style="left:30px;top:74px;width:160px;font-size:3.8px;line-height:1.9;color:#333">
    <p>LUMA_FO is a boutique family office with a holistic approach. We focus on sustaining clients' wealth and overall well-being – while they focus on their families, businesses, and other passions.</p>
    <p style="margin-top:5px">No two families come to us with the same set of needs and objectives. We nurture relationships with each client to help them achieve success – however they define it. The individual attention and access we provide supports a deep, trusting relationship that enables collaboration and high performance.</p>
    <p style="margin-top:5px">We manage clients' projects end to end – wise counsel, strategy, planning, and execution.</p>
  </div>
  <div class="disc" style="left:253px;top:30px;width:85px;height:85px;background:var(--navy);color:#fff;align-items:flex-start;padding-top:30px">APPROACH</div>
  <div class="disc" style="left:201px;top:63px;width:82px;height:82px;background:var(--sky);color:var(--ink);justify-content:flex-start;padding-left:20px">CHARACTER</div>
  <div class="disc" style="left:260px;top:86px;width:85px;height:85px;background:#f2f2f2;border:1px solid #555;color:var(--ink)">END TO END<br>PROJECT<br>MANAGEMENT</div>
  <div class="footer"><div class="brand"><b>BRISCO</b> <span>ENERGY</span></div><div class="num">05</div></div>
</section>

<!-- Slide: roadmap -->
<section class="slide col-a row-4">
  <div class="fill" role="img" aria-label="Faint background of wind turbines over a solar field" style="left:0;right:0;top:90px;bottom:16px;background:linear-gradient(180deg,#fff,#eef0f2)"></div>
  <div class="abs" style="left:0;right:0;top:14px;text-align:center;font-weight:700;font-size:14px;color:#3d3d3d">ROADMAP</div>
  <div class="abs" style="left:122px;top:37px;width:128px;height:1px;background:var(--sky-soft)"></div>
  <svg class="abs" style="left:0;top:0" width="373" height="209" viewBox="0 0 373 209">
    <line x1="75" y1="119" x2="186" y2="119" stroke="#8a8a8a" stroke-width="3"/>
    <line x1="186" y1="119" x2="273" y2="119" stroke="var(--olive)" stroke-width="3"/>
    <line x1="111" y1="104" x2="111" y2="119" stroke="#8a8a8a" stroke-width="1"/>
    <line x1="257" y1="104" x2="257" y2="119" stroke="var(--olive)" stroke-width="1"/>
    <line x1="186" y1="119" x2="186" y2="136" stroke="var(--olive)" stroke-width="1"/>
    <circle cx="111" cy="119" r="2" fill="#fff" stroke="#8a8a8a"/>
    <circle cx="186" cy="119" r="2" fill="#fff" stroke="var(--olive)"/>
    <circle cx="257" cy="119" r="2" fill="#fff" stroke="var(--olive)"/>
    <g transform="translate(111,77) rotate(45)"><rect x="-19" y="-19" width="38" height="38" fill="#fff" stroke="#777" stroke-width="3"/><rect x="-14" y="-14" width="28" height="28" fill="none" stroke="#777" stroke-width=".7"/></g>
    <g transform="translate(257,77) rotate(45)"><rect x="-19" y="-19" width="38" height="38" fill="#fff" stroke="var(--olive)" stroke-width="3"/><rect x="-14" y="-14" width="28" height="28" fill="none" stroke="var(--olive)" stroke-width=".7"/></g>
    <g transform="translate(186,160) rotate(45)"><rect x="-19" y="-19" width="38" height="38" fill="#fff" stroke="var(--olive)" stroke-width="3"/><rect x="-14" y="-14" width="28" height="28" fill="none" stroke="var(--olive)" stroke-width=".7"/></g>
    <g fill="none" stroke="#555" stroke-width="1"><rect x="104" y="71" width="13" height="9"/><circle cx="102" cy="80" r="1.5"/><path d="M106 86h10"/></g>
    <g fill="none" stroke="var(--olive)" stroke-width="1.3"><circle cx="253" cy="79" r="3.5"/><circle cx="261" cy="74" r="2.5"/></g>
    <g fill="none" stroke="#555" stroke-width="1"><rect x="180" y="153" width="11" height="14"/><path d="M182 157h7M182 160h7M182 163h5M188 166l6-8"/></g>
    <g fill="#999"><rect x="89" y="186" width="14" height="2.5" rx="1"/><rect x="89" y="182" width="14" height="2.5" rx="1"/><rect x="89" y="178" width="14" height="2.5" rx="1"/></g>
  </svg>
  <div class="abs" style="left:43px;top:110px;font-family:'Oswald',sans-serif;font-size:13px;color:var(--sky-soft)">2022</div>
  <div class="abs" style="left:296px;top:107px;font-family:'Oswald',sans-serif;font-size:13px;color:var(--navy)">2023</div>
  <div class="road-label" style="left:140px;top:97px;width:92px">Gennaio - Giugno<b>PROGETTAZIONE</b></div>
  <div class="road-label" style="left:70px;top:125px;width:82px">Settembre - Dicembre<b>STUDIO DI FATTIBILITÀ</b></div>
  <div class="road-label" style="left:215px;top:124px;width:90px">Luglio - Dicembre<b>ESECUZIONE PILOTA</b></div>
  <div class="abs" style="left:106px;top:175px;font-family:'Oswald',sans-serif;font-size:10px;color:var(--navy)">≈ 70K</div>
  <div class="footer"><div class="brand"><b>BRISCO</b> <span>ENERGY</span></div><div class="num">06</div></div>
</section>

<!-- Slide: team -->
<section class="slide col-b row-4">
  <div class="rail"></div>
  <div class="rail-year" style="top:80px">2025</div>
  <div class="rail-dot" style="top:100px"></div>
  <div class="abs mono" style="left:37px;top:26px;font-size:13px"><span class="mark">LUMA_FO</span> TEAM</div>
  <div class="abs" style="left:33px;top:68px;width:5px;height:42px;background:linear-gradient(180deg,var(--sky-soft),#2a5fb0)"></div>
  <div class="abs" style="left:184px;top:115px;width:5px;height:42px;background:linear-gradient(180deg,var(--sky-soft),#2a5fb0)"></div>
  <div class="abs" style="left:355px;top:72px;width:5px;height:42px;background:linear-gradient(180deg,var(--sky-soft),#2a5fb0)"></div>
  <div class="member" style="left:36px" role="img" aria-label="Portrait photo of team member"><div class="fill" style="inset:0;background:linear-gradient(180deg,#e9ecef 0%,#b5b8bd 45%,#20242c 80%)"></div><div class="name">ALDO RENNER</div></div>
  <div class="member" style="left:117px" role="img" aria-label="Portrait photo of team member"><div class="fill" style="inset:0;background:linear-gradient(180deg,#eef0f2 0%,#c29a84 45%,#20242c 80%)"></div><div class="name">ALDO RENNER</div></div>
  <div class="member" style="left:198px" role="img" aria-label="Portrait photo of team member"><div class="fill" style="inset:0;background:linear-gradient(180deg,#eef0f2 0%,#c8a48c 40%,#1e2a44 80%)"></div><div class="name">MARCO VITALE</div></div>
  <div class="member" style="left:279px" role="img" aria-label="Portrait photo of team member"><div class="fill" style="inset:0;background:linear-gradient(180deg,#eef0f2 0%,#b08a70 45%,#20242c 80%)"></div><div class="name">CLARA DUNMORE</div></div>
  <div class="values"><span><i></i>CURIOSITY</span><span><i></i>STEWARDSHIP</span><span><i></i>CONTINUITY</span><span><i></i>MANAGEMENT</span></div>
  <div class="footer"><div class="brand"><b>BRISCO</b> <span>ENERGY</span></div><div class="num">07</div></div>
</section>

<!-- Slide: services -->
<section class="slide col-a row-5" style="background:linear-gradient(90deg,#eceef1,#f6f7f9 50%,#e9ecef)">
  <div class="rail"></div>
  <div class="rail-year" style="top:80px;background:transparent">2025</div>
  <div class="rail-dot" style="top:100px"></div>
  <div class="abs mono" style="left:31px;top:19px;font-size:13px"><span class="mark">LUMA_FO</span> SERVICES</div>
  <ul class="svc-box">
    <li>Asset &amp; Performance Reporting</li>
    <li>Business Succession Planning</li>
    <li>Business Acquisition &amp; Exit Planning</li>
    <li>Cash Flow Analysis &amp; Reporting</li>
    <li>Education, Estate, &amp; Legacy Planning</li>
    <li>Executive Compensation Planning</li>
  </ul>
  <div class="abs" style="left:184px;top:63px;width:50px;height:3px;background:var(--sky-soft)"></div>
  <ul class="svc-list">
    <li>Family Advisory Team Coordination &amp;<br>&nbsp;&nbsp;Supervision</li>
    <li>Family Governance &amp; Education</li>
    <li>Financial Administration &amp; Project Management</li>
    <li>Financial Strategy &amp; Planning</li>
    <li>Philanthropy &amp; Impact Planning</li>
    <li>Risk Management</li>
  </ul>
  <div class="abs" style="left:36px;top:123px;font-weight:500;font-size:9px;color:var(--ink)"><span style="color:var(--sky-soft)">Tax Strategy</span> &amp; Consulting</div>
  <p class="abs" style="left:33px;top:149px;width:315px;font-size:5.5px;line-height:1.35;color:#333">Communicate, coordinate, evaluate performance of other advisors. Ensure... Do want your left hand to know what your right hand is doing.<br>Bankers, corporate and estate planning attorneys, insurance agents, public and private investment managers, other investment vehicles (annuities, private credit, local development deal), tax accountants (CPAs), other third-party relationships</p>
  <div class="footer"><div class="brand"><b>BRISCO</b> <span>ENERGY</span></div><div class="num">08</div></div>
</section>

<!-- Slide: closing -->
<section class="slide col-b row-5">
  <div class="fill" role="img" aria-label="Faded landscape with wind turbines on rolling fields" style="inset:0;background:linear-gradient(180deg,#f1f4f7 0%,#f7f8f9 55%,#e4e9e6 100%)"></div>
  <div class="close-wrap">
    <div class="brand-word" style="justify-content:center;font-size:13px"><i style="width:10px;height:10px"></i>Brisco Energy</div>
    <div style="margin-top:18px;font-weight:700;font-size:11.5px;color:var(--navy)">BRISCO <span style="color:var(--sky)">ENERGY</span></div>
    <div style="width:140px;height:1px;background:var(--navy);margin:3px auto 0"></div>
    <div style="margin-top:4px;font-size:6px;color:#222">www.brisco-energy.com</div>
    <div style="margin-top:2px;font-size:4.6px;color:#333;line-height:1.35">Elsa Moravec - Co-Founder elsa@brisco-<br>energy.com +44 (0) 7000 123456</div>
  </div>
</section>

</body>
</html>
```